Web Design - Personal Item Tags Portal

web page designs need to be created for a new company that provides item tracking tags and lets users register and report stolen/found items.
The theme of the designs needs to be energetic and convey a sense of freedom and adventure - where the user does not have to worry about their items since they have all been "tagged".
the client likes parts of the site at: http://www.brisklayouts.example/
they like:
1. slider images at top of pages. large slider on front page. fixed smaller height picture on internal pages
2. fixed company message on left-hand-side
3. My Account button to be clear and stand out

other comments:
clean, simple
• brand focused
• will have clear call to actions
• will include a description of what and why
• will appeal to both males and females

sections that the website will have are:
Home
About Us
How it works
Why
Case Studies
Uses and Applications
Shop
Contact Us

please create 2 designs : 1 home page, 1 internal page

Final winner will also require HTML slicing to be done.
Updates

hi, i have now updated the images so they work. sorry!

Hi, looking at all the designs that are coming in, alot of them are great. Designers need to remember to make the register for an account button more prominent. Also, there should be a "report found" and "report lost" buttons on the front-page and should be prominent as well.

Thanks

Hi, the customer has come back with a few comments and modifications for the designs, if you are able to make some tweaks to your submissions, that will be great:

The client would like the designs to be modified to highlight 3 main actions:
1. Log In/Register
2. Find an Owner
3. Lost an Item

The home page shouldnt be too content heavy in terms of text, it should only have major highlight points of what the system does (the 3 points listed above). the inner page designs are OK to have more text though.

i will also upload some notes from the customer that can be used as a guide and also include the design styles which the customer likes (but is not entirely happy with).

uploaded image files (3) with customer feedback comments

Industry/Entity Type

It Company

```html
<!DOCTYPE html>
<html lang="en">
<head>
<meta charset="utf-8">
<title>KeyRoam – About Us</title>
<link href="https://fonts.googleapis.com/css2?family=Oswald:wght@300;400&family=Jura:wght@500&family=Arimo:wght@400&display=swap" rel="stylesheet">
<style>
  :root {
    --ink: #1e1e1e;
    --muted: #8a8a8a;
    --page: #efefef;
    --rule: #d2d2d2;
    --accent: #1aa7e8;
    --accent-dark: #0c86c7;
    --header-top: #000;
    --header-bottom: #2e2e2e;
    --footer-top: #4a83c0;
    --footer-bottom: #2f5f98;
    --tile: #ececec;
    --tile-edge: #a9a9a9;
    --icon: #666;
  }
  * { box-sizing: border-box; margin: 0; padding: 0; }
  html, body { width: 1200px; height: 988px; overflow: hidden; }
  body {
    position: relative;
    background: linear-gradient(100deg, #f6f6f6 0%, #f3f3f3 55%, #e9e9e9 62%, #ececec 100%);
    font-family: "Arimo", Arial, sans-serif;
    color: var(--ink);
  }
  .site-header {
    position: absolute; left: 0; top: 0; width: 1200px; height: 64px;
    background: linear-gradient(var(--header-top), var(--header-bottom));
    border-bottom: 2px solid var(--accent);
  }
  .brand { position: absolute; left: 303px; top: 9px; display: flex; align-items: center; gap: 10px; }
  .brand-mark { width: 40px; height: 40px; border: 2px solid #fff; border-radius: 50%; }
  .brand-name { font-family: "Oswald", sans-serif; font-weight: 400; font-size: 26px; color: #fff; line-height: 1; }
  .brand-tagline { position: absolute; left: 361px; top: 43px; font-family: "Oswald", sans-serif; font-weight: 300; font-size: 10px; color: #fff; }
  .account-links { position: absolute; right: 304px; top: 7px; display: flex; gap: 5px; }
  .account-links a {
    display: block; height: 13px; padding: 0 6px 0 4px; border-radius: 7px;
    background: var(--accent); color: #fff; font-family: "Oswald", sans-serif; font-size: 8px; line-height: 13px; text-decoration: none;
  }
  .account-links a::before { content: ""; display: inline-block; width: 7px; height: 7px; border-radius: 50%; background: #fff; margin-right: 3px; vertical-align: -1px; }
  .main-nav { position: absolute; right: 303px; top: 31px; display: flex; gap: 16px; }
  .main-nav a { font-family: "Oswald", sans-serif; font-weight: 300; font-size: 11px; color: #fff; text-decoration: none; }
  .main-nav a.is-current { color: var(--accent); }

  .hero { position: absolute; left: 0; top: 64px; width: 1200px; height: 138px; }
  .hero-photo {
    position: absolute; inset: 0;
    background: linear-gradient(90deg, #2f6fae 0%, #3b7dbd 26%, #2a5c8e 34%, #0a0a0a 44%, #000 100%);
  }
  .hero-title { position: absolute; left: 541px; top: 52px; font-family: "Jura", sans-serif; font-weight: 500; font-size: 45px; line-height: 1; color: var(--accent); }
  .hero-subtitle { position: absolute; left: 622px; top: 98px; font-family: "Jura", sans-serif; font-weight: 500; font-size: 25px; line-height: 1; color: var(--accent); }

  .section-title { position: absolute; font-family: "Oswald", sans-serif; font-weight: 300; font-size: 19px; color: var(--ink); }
  .copy { position: absolute; font-size: 8.2px; line-height: 13.8px; color: var(--muted); text-align: justify; }
  .about-photo { position: absolute; left: 306px; top: 311px; width: 246px; height: 171px; border: 2px solid #c9c9c9; background: linear-gradient(#8a9aa6, #5f7a78 55%, #3e5c63); }
  .rule-h { position: absolute; left: 302px; width: 596px; height: 1px; background: var(--rule); }
  .rule-v { position: absolute; left: 600px; top: 555px; width: 1px; height: 175px; background: var(--rule); }
  .read-more { position: absolute; display: flex; align-items: center; gap: 6px; font-family: "Oswald", sans-serif; font-weight: 300; font-size: 19px; color: var(--accent); text-decoration: none; }
  .feature-icon { position: absolute; }

  .product-tile { position: absolute; top: 791px; width: 119px; height: 97px; background: var(--tile); border: 3px solid var(--tile-edge); display: flex; align-items: center; justify-content: center; }
  .shop-button {
    position: absolute; left: 801px; top: 816px; width: 96px; height: 40px; border-radius: 6px;
    background: linear-gradient(var(--accent), var(--accent-dark));
    font-family: "Oswald", sans-serif; font-weight: 300; font-size: 19px; color: #fff; text-align: center; line-height: 38px; text-decoration: none;
  }
  .shop-links { position: absolute; left: 806px; top: 861px; font-family: "Oswald", sans-serif; font-weight: 300; font-size: 10px; color: #333; word-spacing: 1px; }

  .site-footer { position: absolute; left: 0; top: 925px; width: 1200px; height: 63px; background: linear-gradient(var(--footer-top), var(--footer-bottom)); }
  .copyright { position: absolute; left: 0; width: 1200px; top: 13px; text-align: center; font-size: 8.5px; color: #fff; }
  .social { position: absolute; left: 563px; top: 31px; display: flex; gap: 3px; }
  .social span { width: 22px; height: 22px; border-radius: 50%; background: #fff; }
</style>
</head>
<body>
  <header class="site-header">
    <div class="brand"><span class="brand-mark"></span><span class="brand-name">KeyRoam</span></div>
    <div class="brand-tagline">. . . adventure first</div>
    <nav class="account-links"><a href="#">My Account</a><a href="#">My Cart</a></nav>
    <nav class="main-nav">
      <a href="#">Home</a><a href="#" class="is-current">About Us</a><a href="#">How it Works ?</a><a href="#">Why ?</a><a href="#">Case Studies</a><a href="#">Uses &amp; Applications</a><a href="#">Shop</a><a href="#">Contact Us</a>
    </nav>
  </header>

  <section class="hero">
    <div class="hero-photo" role="img" aria-label="Rock climber silhouetted on a cliff edge against blue sky"></div>
    <h1 class="hero-title">‘Adventure First’</h1>
    <p class="hero-subtitle">Intrepid TAG Solutions</p>
  </section>

  <h2 class="section-title" style="left:306px;top:260px">About Us</h2>
  <div class="about-photo" role="img" aria-label="Adventurer on a zip line over a mountain fjord"></div>
  <p class="copy" style="left:574px;top:306px;width:319px">Lorem ipsum dolor sit amet, consectetuer adipiscing elit, sed diam nonummy nibh euismod tincidunt ut laoreet dolore magna aliquam erat volutpat. Ut wisi enim ad minim veniam, quis nostrud exerci tation ullamcorper suscipit lobortis nisl ut aliquip ex ea commodo consequat. Duis autem vel eum iriure dolor in hendrerit in vulputate velit esse molestie consequat, vel illum dolore eu feugiat nulla facilisis at vero eros et accumsan et iusto odio dignissim qui blandit praesent luptatum zzril delenit augue duis dolore te feugait nulla facilisi. Nam liber tempor cum</p>
  <p class="copy" style="left:574px;top:417px;width:319px">Lorem ipsum dolor sit amet, consectetuer adipiscing elit, sed diam nonummy nibh euismod tincidunt ut laoreet dolore magna aliquam erat volutpat. Ut wisi enim ad minim veniam, quis nostrud exerci tation ullamcorper suscipit lobortis nisl ut aliquip ex ea commodo consequat. Duis autem vel eum iriure dolor in hendrerit in vulputate velit esse molestie consequat, vel illum dolore eu feugiat.</p>

  <div class="rule-h" style="top:522px"></div>

  <h2 class="section-title" style="left:306px;top:549px">How it Works ?</h2>
  <svg class="feature-icon" style="left:323px;top:606px" width="24" height="62" viewBox="0 0 24 62" aria-hidden="true">
    <path d="M6 2h12v7h-4v21h-4V9H6z" fill="none" stroke="#9a9a9a" stroke-width="2.5"/>
    <path d="M4 32h16v18c0 6-8 11-8 11s-8-5-8-11z" fill="#9a9a9a"/>
  </svg>
  <p class="copy" style="left:384px;top:603px;width:199px">Lorem ipsum dolor sit amet, consectetuer adipiscing elit, sed diam nonummy nibh euismod tincidunt ut laoreet dolore magna aliquam erat volutpat. Ut wisi enim ad minim veniam, quis nostrud exerci tation ullamcorper suscipit lobortis nisl ut ....</p>
  <a class="read-more" href="#" style="left:306px;top:686px">Read More
    <svg width="26" height="20" viewBox="0 0 26 20" aria-hidden="true"><path d="M2 2l9 8-9 8" fill="none" stroke="var(--accent)" stroke-width="3"/><path d="M12 2l9 8-9 8" fill="none" stroke="#9fd8f4" stroke-width="3"/></svg>
  </a>

  <div class="rule-v"></div>

  <h2 class="section-title" style="left:618px;top:549px">Why Us ?</h2>
  <svg class="feature-icon" style="left:622px;top:607px" width="58" height="58" viewBox="0 0 58 58" aria-hidden="true">
    <circle cx="29" cy="29" r="29" fill="#b5b5b5"/>
    <circle cx="31" cy="15" r="4" fill="#fff"/>
    <path d="M27 23h7l-4 22h-7z" fill="#fff"/>
  </svg>
  <p class="copy" style="left:696px;top:603px;width:199px">Lorem ipsum dolor sit amet, consectetuer adipiscing elit, sed diam nonummy nibh euismod tincidunt ut laoreet dolore magna aliquam erat volutpat. Ut wisi enim ad minim veniam, quis nostrud exerci tation ullamcorper suscipit lobortis nisl ut ....</p>
  <a class="read-more" href="#" style="left:618px;top:686px">Read More
    <svg width="26" height="20" viewBox="0 0 26 20" aria-hidden="true"><path d="M2 2l9 8-9 8" fill="none" stroke="var(--accent)" stroke-width="3"/><path d="M12 2l9 8-9 8" fill="none" stroke="#9fd8f4" stroke-width="3"/></svg>
  </a>

  <div class="rule-h" style="top:757px"></div>

  <div class="product-tile" style="left:302px"><svg width="86" height="70" viewBox="0 0 86 70" aria-hidden="true"><path d="M43 14L4 4l-2 18 41 8 41-8-2-18zM10 30l33 6 33-6v32l-33 8-33-8z" fill="var(--icon)"/></svg></div>
  <div class="product-tile" style="left:427px"><svg width="86" height="70" viewBox="0 0 86 70" aria-hidden="true"><path d="M43 14L4 4l-2 18 41 8 41-8-2-18zM10 30l33 6 33-6v32l-33 8-33-8z" fill="var(--icon)"/></svg></div>
  <div class="product-tile" style="left:552px"><svg width="86" height="70" viewBox="0 0 86 70" aria-hidden="true"><path d="M43 14L4 4l-2 18 41 8 41-8-2-18zM10 30l33 6 33-6v32l-33 8-33-8z" fill="var(--icon)"/></svg></div>
  <div class="product-tile" style="left:677px"><svg width="86" height="70" viewBox="0 0 86 70" aria-hidden="true"><path d="M43 14L4 4l-2 18 41 8 41-8-2-18zM10 30l33 6 33-6v32l-33 8-33-8z" fill="var(--icon)"/></svg></div>

  <a class="shop-button" href="#">Visit Shop</a>
  <p class="shop-links">Login &nbsp;|&nbsp; View All &nbsp;|&nbsp; Sign Up</p>

  <footer class="site-footer">
    <p class="copyright">© 2013 Keyroam. All rights reserved.</p>
    <div class="social" aria-label="Social links"><span></span><span></span><span></span></div>
  </footer>
</body>
</html>
```